Casa Vero Inspections Business Card

I need a business card for my new company. The company is going to provide home inspections. The name of the company is Casa Vero Inspections. I am not sure if I want a single sided card or a double. I have a logo already that I want to incorporate into the card design. I was wondering if I should incorporate a catch phrase on my card or not. If I did the phrase would be "The Intelligent Choice for Home Inspections" but i am unsure how or if to use it on a card. The following information needs to be on the card.
Home Inspection
My Name: Marcus T. Wolford Phone Number: 555-301-7762 Email: mwolford@casaveroinspections.com Website: www.casaveroinspections.com NY HI License # 27300519462

```html
<!DOCTYPE html>
<html lang="en">
<head>
<meta charset="utf-8">
<title>Casa Vero Inspections – Business Card</title>
<link href="https://fonts.googleapis.com/css2?family=Montserrat:wght@500;600;700&display=swap" rel="stylesheet">
<style>
  :root {
    --backdrop: #686868;
    --card-white: #ffffff;
    --brand-navy: #045686;
    --brand-blue: #0b6aa6;
    --sky: #7cc4ee;
    --text-light: #ffffff;
  }
  html, body {
    margin: 0;
    padding: 0;
    width: 1200px;
    height: 1200px;
    overflow: hidden;
    background: var(--backdrop);
    font-family: "Montserrat", sans-serif;
  }
  .card {
    position: absolute;
    left: 202px;
    width: 796px;
    height: 442px;
    box-sizing: border-box;
  }
  .card--front {
    top: 117px;
    background: var(--card-white);
    display: flex;
    align-items: center;
    justify-content: center;
  }
  .brand {
    display: flex;
    align-items: center;
    gap: 16px;
    margin-top: -12px;
  }
  .brand__mark {
    width: 30px;
    height: 30px;
    background: var(--brand-blue);
  }
  .brand__name {
    font-weight: 700;
    font-size: 40px;
    letter-spacing: 0.5px;
    color: var(--brand-blue);
  }
  .card--back {
    top: 616px;
    background: var(--brand-navy);
    color: var(--text-light);
    padding: 114px 0 0 68px;
  }
  .holder-name {
    margin: 0 0 24px;
    font-weight: 600;
    font-size: 37px;
    line-height: 1;
  }
  .contact-list {
    list-style: none;
    margin: 0;
    padding: 0;
  }
  .contact-item {
    display: flex;
    align-items: center;
    gap: 14px;
    height: 34px;
    margin-bottom: 6px;
    font-weight: 500;
    font-size: 23px;
  }
  .contact-icon {
    width: 34px;
    height: 34px;
    background: var(--sky);
    display: flex;
    align-items: center;
    justify-content: center;
    flex-shrink: 0;
  }
  .license {
    margin: 20px 0 0;
    font-weight: 500;
    font-size: 23px;
  }
</style>
</head>
<body>
  <section class="card card--front" aria-label="Card front">
    <div class="brand">
      <span class="brand__mark" aria-hidden="true"></span>
      <span class="brand__name">Casa Vero Inspections</span>
    </div>
  </section>

  <section class="card card--back" aria-label="Card back">
    <h1 class="holder-name">Marcus T. Wolford</h1>
    <ul class="contact-list">
      <li class="contact-item">
        <span class="contact-icon">
          <svg width="20" height="20" viewBox="0 0 24 24" aria-hidden="true"><path fill="#fff" d="M6.6 10.8a15.1 15.1 0 0 0 6.6 6.6l2.2-2.2c.3-.3.7-.4 1-.2 1.1.4 2.3.6 3.6.6.6 0 1 .4 1 1V20c0 .6-.4 1-1 1C10.6 21 3 13.4 3 4c0-.6.4-1 1-1h3.5c.6 0 1 .4 1 1 0 1.3.2 2.5.6 3.6.1.3 0 .7-.2 1z"/></svg>
        </span>
        <span>555-301-7762</span>
      </li>
      <li class="contact-item">
        <span class="contact-icon">
          <svg width="22" height="16" viewBox="0 0 22 16" aria-hidden="true"><rect x="1" y="1" width="20" height="14" fill="none" stroke="#fff" stroke-width="1.6"/><path d="M1 1l10 8 10-8M1 15l7-6M21 15l-7-6" fill="none" stroke="#fff" stroke-width="1.6"/></svg>
        </span>
        <span>mwolford@casaveroinspections.com</span>
      </li>
      <li class="contact-item">
        <span class="contact-icon">
          <svg width="20" height="20" viewBox="0 0 20 20" aria-hidden="true"><g fill="none" stroke="#fff" stroke-width="1.4"><circle cx="10" cy="10" r="8.5"/><ellipse cx="10" cy="10" rx="4" ry="8.5"/><path d="M1.5 10h17M3 5.5h14M3 14.5h14"/></g></svg>
        </span>
        <span>casaveroinspections.com</span>
      </li>
    </ul>
    <p class="license">NY HI License # 27300519462</p>
  </section>
</body>
</html>
```